Web Developer Needs a Business Card Design

I need a personal business card design that represents me as a web developer for potential employers. I would like the background to be a dark color on the front for contrast with my logo and name. The back will have all my information along with a smaller version of the logo. I want something with a modern look and feel, not too conservative. This will be used for potential employers and freelance work.

Industry/Entity Type

Business

Contact Information for Business Card

Front should have my logo and name. The back should have all my personal information which would include: name: Tom Brevardi, phone: 570-614-9083, email: tombrevardi@mailwisp.com, website url: www.tombrevardi.com, logo, web developer.

Font styles to use
Sans Serif

Requirements
Must have
• Must include my logo. The color palette base color will be the logo color.

```html
<!DOCTYPE html>
<html lang="en">
<head>
<meta charset="utf-8">
<title>Tom Brevardi — Business Card</title>
<link rel="stylesheet" href="https://fonts.googleapis.com/css2?family=Marcellus+SC&display=swap">
<style>
  :root {
    --page-bg: #e4e5e7;
    --navy-deep: #0f1f5c;
    --navy: #16297a;
    --navy-glow: #1d3390;
    --teal: #4ae3bf;
    --ink: #27306f;
  }
  * { margin: 0; padding: 0; box-sizing: border-box; }
  html, body {
    width: 1200px;
    height: 1192px;
    overflow: hidden;
    background: var(--page-bg);
  }
  .card {
    position: absolute;
    left: 262px;
    width: 676px;
    height: 396px;
    border-radius: 13px;
    overflow: hidden;
    font-family: "Marcellus SC", serif;
  }
  .card--front {
    top: 144px;
    background: var(--navy);
  }
  .front-artwork {
    position: absolute;
    inset: 0;
    background: radial-gradient(ellipse at 50% 35%, var(--navy-glow) 0%, var(--navy) 55%, var(--navy-deep) 100%);
  }
  .front-mark {
    position: absolute;
    left: 226px;
    top: 94px;
    width: 192px;
    height: 192px;
    border: 10px solid var(--teal);
    border-radius: 50%;
    display: flex;
    align-items: center;
    justify-content: center;
  }
  .front-mark__name {
    color: var(--teal);
    font-size: 22px;
    letter-spacing: 0.5px;
    white-space: nowrap;
  }
  .card--back {
    top: 621px;
    background: var(--teal);
    color: var(--ink);
  }
  .back-mark {
    position: absolute;
    left: -36px;
    top: 111px;
    width: 220px;
    height: 220px;
    border: 13px solid var(--ink);
    border-radius: 50%;
  }
  .back-mark__name {
    position: absolute;
    left: 10px;
    top: 208px;
    width: 160px;
    text-align: center;
    font-size: 19px;
    color: var(--ink);
    white-space: nowrap;
  }
  .holder-name {
    position: absolute;
    right: 50px;
    top: 50px;
    font-size: 22px;
    letter-spacing: 0.3px;
  }
  .contact-list {
    position: absolute;
    left: 188px;
    top: 184px;
    list-style: none;
  }
  .contact-list li {
    display: flex;
    align-items: center;
    height: 29px;
    font-size: 19px;
    letter-spacing: 0.2px;
  }
  .contact-list .phone-number { font-size: 21px; }
  .contact-icon {
    width: 18px;
    height: 18px;
    margin-right: 10px;
    flex: none;
  }
</style>
</head>
<body>

<section class="card card--front">
  <div class="front-artwork" role="img" aria-label="Navy-toned image of a laptop, tablet and phone linked by a network of user icons, with faint silhouettes of people"></div>
  <div class="front-mark">
    <span class="front-mark__name">Tom Brevardi</span>
  </div>
</section>

<section class="card card--back">
  <div class="back-mark"></div>
  <span class="back-mark__name">Tom Brevardi</span>

  <h1 class="holder-name" style="font-weight:400">Tom Brevardi</h1>

  <ul class="contact-list">
    <li>
      <svg class="contact-icon" viewBox="0 0 20 20" aria-hidden="true">
        <circle cx="10" cy="10" r="8" fill="none" stroke="var(--ink)" stroke-width="1.6"/>
        <path d="M8 5.5c-1.6 1.2-1.6 7.8 0 9l1.4-1.6c-.7-1.2-.7-4.6 0-5.8z" fill="var(--ink)"/>
      </svg>
      <span class="phone-number">570-614-9083</span>
    </li>
    <li>
      <svg class="contact-icon" viewBox="0 0 20 20" aria-hidden="true">
        <rect x="1" y="4" width="18" height="12" fill="var(--ink)"/>
        <path d="M1.5 4.5l8.5 6.5 8.5-6.5M1.5 15.5l6-5.5M18.5 15.5l-6-5.5" fill="none" stroke="var(--teal)" stroke-width="1.2"/>
      </svg>
      <span>TOMBREVARDI@MAILWISP.COM</span>
    </li>
    <li>
      <svg class="contact-icon" viewBox="0 0 20 20" aria-hidden="true">
        <g fill="none" stroke="var(--ink)" stroke-width="1.4">
          <circle cx="10" cy="10" r="8"/>
          <ellipse cx="10" cy="10" rx="3.5" ry="8"/>
          <path d="M2 10h16M3.2 6h13.6M3.2 14h13.6"/>
        </g>
      </svg>
      <span>WWW.TOMBREVARDI.COM</span>
    </li>
  </ul>
</section>

</body>
</html>
```